KRANO study results infographic

We enjoyed the previous infographic design you provided for us (The GaRVU cohort study Infographic), and would like to invite you to design another infographic in a similar style and layout.
We need an infographic which presents the results from the KRANO research trial. It should be colourful and engaging, in understandable language and showing the steps to get to the results. This is to showcase the results to patients/the public/clinicians, giving a brief summary of what the study proved. The final design should have the KRANO logo at the top (please see attached and https://krano.pelbu.quenmarsh.example/welcome-krano-trial)
I have attached the required logos which need to be used (KRANO, Penhallow Injury and Acute Care, University of Castlemere) as well as an example from another study, The GaRVU cohort study Infographic, as an example of what the layout could look like. Please DO NOT use the content from the The GaRVU cohort study Infographic example though, please instead use the content from the attached document 'KRANO_InfographicDesignInformation_Plinthwork'.

```html
<!DOCTYPE html>
<html lang="en">
<head>
<meta charset="utf-8">
<title>KRANO study results infographic</title>
<link href="https://fonts.googleapis.com/css2?family=Poppins:wght@400;500;600;700;800&display=swap" rel="stylesheet">
<style>
  :root{
    --navy:#213862;
    --blue:#2fa6de;
    --pale:#e6f1fa;
    --ink:#1c2a47;
    --white:#ffffff;
    --ring:#9fd0ee;
    --grey:#6d7483;
    --red:#c8313d;
  }
  *{margin:0;padding:0;box-sizing:border-box}
  html,body{width:1200px;height:2792px;overflow:hidden;background:var(--white)}
  body{font-family:'Poppins',sans-serif;color:var(--ink);position:relative}
  .abs{position:absolute}
  .backdrop{position:absolute;left:0;top:0}
  .brand{left:0;width:1200px;top:62px;color:var(--white);font-weight:700;font-size:56px;letter-spacing:2px;display:flex;justify-content:center;align-items:center;gap:14px}
  .brand .dot{width:30px;height:30px;border-radius:50%;background:var(--blue)}
  .title{left:0;width:1200px;top:182px;text-align:center;color:var(--white);font-weight:800;font-size:27.5px;line-height:29.5px;letter-spacing:-.3px;text-transform:uppercase;white-space:nowrap}
  .title .accent{color:var(--blue)}
  .intro-head{left:76px;top:450px;font-weight:700;font-size:32px;line-height:39px;color:var(--navy);text-transform:uppercase}
  .intro-head .sub{display:block;color:var(--blue);font-weight:400;font-size:32px;margin-top:2px}
  .intro-text{left:74px;top:630px;width:530px;font-size:19px;line-height:29px;color:var(--ink)}
  .intro-art{left:628px;top:434px;width:530px;height:406px;border-radius:50% 45% 40% 50%;background:linear-gradient(135deg,#eef6fd,#d7eaf8)}
  .section-head{font-weight:800;color:var(--blue);font-size:36px;letter-spacing:.5px;text-transform:uppercase}
  .findings-head{left:0;width:1200px;top:936px;text-align:center}
  .finding{text-align:center;font-weight:600;font-size:17.5px;line-height:26px;color:var(--navy)}
  .elig-head{left:476px;top:1352px;color:var(--white);font-size:33px;font-weight:800}
  .elig-bar{left:479px;top:1414px;width:3px;height:102px;background:var(--white)}
  .elig-text{left:498px;top:1406px;width:590px;font-size:21.5px;line-height:29px;color:var(--white)}
  .elig-art{left:170px;top:1323px;width:250px;height:250px;border-radius:50%;background:linear-gradient(160deg,#ffffff,#eaf4fb)}
  .details-head{left:108px;top:1660px}
  .detail{font-size:21.5px;line-height:29px;color:var(--ink)}
  .audience-head{left:0;width:1200px;top:2134px;text-align:center}
  .aud-label{width:150px;text-align:center;top:2312px;font-weight:600;font-size:16.5px;line-height:21px;color:var(--navy)}
  .uni{left:109px;top:2464px;width:200px;height:200px;border-radius:50%;background:var(--navy);color:var(--white);display:flex;flex-direction:column;align-items:center;justify-content:center;text-align:center;gap:6px}
  .uni .dot{width:26px;height:26px;border-radius:50%;border:2px solid var(--white)}
  .uni .name{font-size:15px;line-height:20px;font-weight:500}
  .sponsor-head{left:365px;top:2476px;color:var(--blue);font-size:25px;font-weight:700}
  .sponsor-text{left:365px;top:2518px;width:680px;font-size:18.5px;line-height:29px;font-weight:600;color:var(--navy)}
  .partner{left:366px;top:2628px;display:flex;align-items:center;gap:8px;font-size:21px;color:var(--grey);font-weight:400}
  .partner .sq{width:22px;height:22px;background:var(--red)}
  .footer{left:0;top:2699px;width:1200px;height:93px;background:var(--navy);color:var(--white);display:flex;align-items:center;justify-content:center;gap:40px;font-size:24px}
  .footer b{font-weight:600}
  .footer .mail{display:flex;align-items:center;gap:14px;font-weight:600;font-size:22px}
</style>
</head>
<body>
<svg class="backdrop" width="1200" height="2792" viewBox="0 0 1200 2792" aria-hidden="true">
  <polygon points="0,0 1200,0 1200,306 0,406" fill="#213862"/>
  <polygon points="700,352 1200,304 1200,418" fill="#2fa6de"/>
  <polygon points="0,940 1200,840 1200,2141 0,2065" fill="#e6f1fa"/>
  <polygon points="0,2065 335,2086 0,2141" fill="#2fa6de"/>
  <line x1="238" y1="1061" x2="980" y2="1061" stroke="#7fb7dc" stroke-width="1.5" stroke-dasharray="3 3"/>
  <circle cx="321" cy="1061" r="5" fill="#2fa6de"/>
  <circle cx="613" cy="1061" r="5" fill="#2fa6de"/>
  <circle cx="897" cy="1061" r="5" fill="#2fa6de"/>
  <g fill="#fff" stroke="#2fa6de" stroke-width="4">
    <circle cx="184" cy="1057" r="54"/>
    <circle cx="460" cy="1057" r="54"/>
    <circle cx="752" cy="1052" r="54"/>
    <circle cx="1034" cy="1057" r="54"/>
  </g>
  <g fill="none" stroke="#213862" stroke-width="2.5">
    <circle cx="172" cy="1037" r="7"/><circle cx="196" cy="1037" r="7"/>
    <circle cx="163" cy="1054" r="7"/><circle cx="184" cy="1054" r="7"/><circle cx="205" cy="1054" r="7"/>
    <path d="M152 1080 v-10 q11 -9 22 0 v10 M174 1080 v-10 q11 -9 21 0 v10 M195 1080 v-10 q11 -9 21 0 v10"/>
  </g>
  <g fill="none" stroke="#213862" stroke-width="2.5">
    <rect x="436" y="1034" width="48" height="46" rx="4"/>
    <line x1="436" y1="1046" x2="484" y2="1046"/>
    <line x1="446" y1="1028" x2="446" y2="1038"/><line x1="474" y1="1028" x2="474" y2="1038"/>
    <path d="M444 1055h6M456 1055h6M468 1055h6M444 1064h6M456 1064h6M444 1073h6M456 1073h6"/>
    <circle cx="482" cy="1076" r="9" fill="#fff"/>
    <path d="M482 1071v5h4"/>
  </g>
  <g fill="none" stroke="#213862" stroke-width="2.5">
    <path d="M762 1028 a7 7 0 1 1 8 10 l-20 34 a7 7 0 1 1 -10 8 a7 7 0 1 1 2 -12 l20 -34 a7 7 0 0 1 0 -6z"/>
  </g>
  <g fill="none" stroke="#213862" stroke-width="2.5">
    <rect x="1014" y="1030" width="40" height="52" rx="4"/>
    <rect x="1024" y="1025" width="20" height="9" rx="2" fill="#fff"/>
    <path d="M1034 1042v12M1028 1048h12"/>
    <path d="M1022 1062h6M1032 1062h16M1022 1071h6M1032 1071h16"/>
  </g>
  <rect x="89" y="1279" width="1052" height="338" fill="#2fa6de"/>
  <polygon points="89,1279 374,1279 210,1617 89,1617" fill="#213862"/>
  <circle cx="295" cy="1448" r="128" fill="none" stroke="#ffffff" stroke-width="2" stroke-dasharray="2 4"/>
  <line x1="123" y1="1753" x2="123" y2="1965" stroke="#2fa6de" stroke-width="1.5"/>
  <line x1="675" y1="1748" x2="675" y2="2019" stroke="#2fa6de" stroke-width="1.5"/>
  <g fill="#fff" stroke="#2fa6de" stroke-width="2.5">
    <circle cx="123" cy="1753" r="9"/><circle cx="123" cy="1843" r="9"/><circle cx="123" cy="1905" r="9"/><circle cx="123" cy="1965" r="9"/>
    <circle cx="675" cy="1748" r="9"/><circle cx="675" cy="1810" r="9"/><circle cx="675" cy="1901" r="9"/><circle cx="675" cy="2019" r="9"/>
  </g>
  <g fill="#fff" stroke="#9fd0ee" stroke-width="1.5" stroke-dasharray="2 3">
    <circle cx="185" cy="2295" r="98"/><circle cx="396" cy="2295" r="98"/><circle cx="605" cy="2295" r="98"/><circle cx="809" cy="2295" r="98"/><circle cx="1015" cy="2295" r="98"/>
  </g>
  <circle cx="185" cy="2258" r="37" fill="#2fa6de"/>
  <circle cx="396" cy="2258" r="37" fill="#213862"/>
  <circle cx="605" cy="2258" r="37" fill="#2fa6de"/>
  <circle cx="809" cy="2258" r="37" fill="#213862"/>
  <circle cx="1015" cy="2258" r="37" fill="#2fa6de"/>
</svg>

<div class="abs brand"><span class="dot"></span>KRANO</div>
<h1 class="abs title">A feasibility study of standard dressings versus<br>negative-pressure wound therapy in the treatment of<br>adult patients having surgical incisions for hip fractures:<br><span class="accent">The KRANO randomized controlled trial</span></h1>

<h2 class="abs intro-head">Hip fracture surgery: can<br>‘vacuum’ dressings<br>reduce deep infections?<span class="sub">(Feasibility trial)</span></h2>
<p class="abs intro-text">Adults &gt;65 years undergoing hip fracture surgery at 5 UK centres were randomised to standard dressings or negative pressure ‘vacuum’ dressings (called iNPWT). Deep infection (CDC-defined) was assessed at 30 &amp; 90 days; other outcomes like Health Related Quality of Life were assessed at 120 days. The overall deep SSI rate was ~4%; effect signals favoured iNPWT, and a definitive trial was deemed feasible.</p>
<div class="abs intro-art" role="img" aria-label="Illustration of a clinician with a tablet beside a pelvis diagram and an older patient in a wheelchair"></div>

<h2 class="abs section-head findings-head">Findings</h2>
<p class="abs finding" style="left:60px;top:1116px;width:240px">462 valid randomisations; recruitment rate ~62% of eligible cases.</p>
<p class="abs finding" style="left:306px;top:1140px;width:310px">Deep SSI at 30 days:<br>6.4% (standard) vs 1.9% (iNPWT) at 90 days: 6.4% vs 2.3%.</p>
<p class="abs finding" style="left:642px;top:1116px;width:220px">Overall 30-day deep SSI 4.2% for hip fracture population</p>
<p class="abs finding" style="left:917px;top:1140px;width:240px">Feasibility confirmed for a fully powered effectiveness trial.</p>

<div class="abs elig-art" role="img" aria-label="Illustration of two older adults, one in a wheelchair and one with a walking stick"></div>
<h2 class="abs elig-head">ELIGIBILITY CRITERIA</h2>
<div class="abs elig-bar"></div>
<p class="abs elig-text">Inclusion: age &gt;<b>65 years</b>; undergoing any surgery for hip fracture. Exclusion: undisplaced intracapsular fracture treated with cannulated screws; other factors precluding participation.</p>

<h2 class="abs section-head details-head">Study details</h2>
<p class="abs detail" style="left:145px;top:1737px;width:420px">Design: Two-arm multicentre RCT embedded in the GaRVU cohort</p>
<p class="abs detail" style="left:145px;top:1828px">Sites: 5 UK centres</p>
<p class="abs detail" style="left:145px;top:1890px">Participants: 462 randomised</p>
<p class="abs detail" style="left:145px;top:1951px">Recruitment: Jul 2017–Feb 2018</p>
<p class="abs detail" style="left:700px;top:1733px">Follow-up to 120 days</p>
<p class="abs detail" style="left:700px;top:1795px;width:400px">Primary outcome: deep SSI at 30 &amp; 90 days (CDC)</p>
<p class="abs detail" style="left:700px;top:1886px;width:430px">Secondary: recruitment metrics, further surgery, EQ-5D-5L, complications, mobility, residential status</p>
<p class="abs detail" style="left:700px;top:2005px">Registration: ISRCTN48217390.</p>

<h2 class="abs section-head audience-head">Target audience</h2>
<p class="abs aud-label" style="left:110px">Orthopaedic &amp; Trauma Clinicians</p>
<p class="abs aud-label" style="left:321px">Orthogeriatric Teams</p>
<p class="abs aud-label" style="left:530px">Infection Prevention Leads</p>
<p class="abs aud-label" style="left:734px">Commissioners</p>
<p class="abs aud-label" style="left:940px">Patient/Public Audiences</p>

<div class="abs uni"><span class="dot"></span><span class="name">UNIVERSITY OF<br>CASTLEMERE</span></div>
<h2 class="abs sponsor-head">SPONSOR</h2>
<p class="abs sponsor-text">Royal Guild of Surgical Practice/Ashcombe Medical Trust (training fellowship), National Castlemere Biomedical Research Centre (infrastructure support), Merrow &amp; Vale (device supply).</p>
<div class="abs partner"><span class="sq"></span>PENHALLOW INJURY &amp; ACUTE CARE</div>

<footer class="abs footer">
  <span>Chief Investigator: <b>Elena Varrow</b></span>
  <span class="mail">
    <svg width="36" height="36" viewBox="0 0 36 36" aria-hidden="true"><circle cx="18" cy="18" r="18" fill="#2fa6de"/><rect x="9" y="12" width="18" height="12" rx="1.5" fill="none" stroke="#fff" stroke-width="2"/><path d="M9 13l9 7 9-7" fill="none" stroke="#fff" stroke-width="2"/></svg>
    elena.varrow@krano-trial.example
  </span>
</footer>
</body>
</html>
```